Fontenot Bayou Grillhouse (Owners Card)

Need a classy, but modern business card. I have included a promotional card for the steakhouse. I need one for myself (the owner) that is more professional.

Target Market(s)

General Public

Industry/Entity Type

Food service

Contact Information for Business Card

Name, business address, phone number, email, logo

Font styles to use
Serif
Sans Serif
Decorative
Script

Requirements
Must have
• My name (Darvel Pruitt), business address (327 Oakmere Street), phone number (510) 493-2615, email (Dpruittkr4@mailvane.example. On the back of the card: Psalms 27 1 The LORD is my light and my salvation— whom shall I fear? The LORD is the stronghold of my life— of whom shall I be afraid? 2 When the wicked advance against me to devour me, it is my enemies and my foes who will stumble and fall. 3 Though an army besiege me, my heart will not fear; though war break out against me, even then I will be confident.
Nice to have
• Something that’s bold, but modern and professional.

```html
<!DOCTYPE html>
<html lang="en">
<head>
<meta charset="utf-8">
<title>Fontenot Bayou Grillhouse – Owner Card</title>
<link href="https://fonts.googleapis.com/css2?family=Cinzel:wght@600;700&family=Prata&family=Poppins:wght@400;500;700;800&display=swap" rel="stylesheet">
<style>
  :root {
    --stage: #adadad;
    --card-dark: #060404;
    --card-light: #ffffff;
    --green: #22e01c;
    --yellow: #f2b705;
    --orange: #ff8a00;
    --red: #f20d0d;
    --ink: #111111;
    --white: #ffffff;
    --brand-grad: linear-gradient(90deg, var(--green) 0%, var(--yellow) 45%, var(--orange) 65%, var(--red) 100%);
  }
  * { box-sizing: border-box; margin: 0; padding: 0; }
  html, body { width: 974px; height: 1200px; overflow: hidden; }
  body { background: var(--stage); position: relative; font-family: "Poppins", sans-serif; }

  .card {
    position: absolute; left: 136px; width: 702px; height: 401px;
    box-shadow: 0 10px 22px rgba(0,0,0,.28);
    overflow: hidden;
  }
  .card--front { top: 140px; background: var(--card-dark); }
  .card--back { top: 663px; background: var(--card-light); }

  .brand-mark { position: absolute; display: flex; flex-direction: column; align-items: center; }
  .brand-mark__dot { width: 44px; height: 44px; border-radius: 50%; background: var(--orange); margin-bottom: 14px; }
  .brand-mark__name {
    font-family: "Cinzel", serif; font-weight: 700; color: var(--orange);
    text-align: center; line-height: 1.1; letter-spacing: 1px;
  }
  .card--front .brand-mark { left: 0; right: 0; top: 60px; }
  .card--front .brand-mark__name { font-size: 30px; }

  .verse__quote {
    position: absolute; font-family: "Prata", serif; color: transparent;
    -webkit-text-stroke: 1.5px var(--red); font-size: 70px; line-height: 1;
  }
  .verse__quote--open { left: 62px; top: 196px; }
  .verse__quote--close { left: 590px; top: 292px; }
  .verse__lead { position: absolute; left: 0; right: 0; top: 235px; text-align: center; font-family: "Prata", serif; font-size: 21px; color: var(--yellow); }
  .verse__follow { position: absolute; left: 0; right: 0; top: 262px; text-align: center; font-family: "Prata", serif; font-size: 15.5px; color: var(--white); }
  .verse__ref { position: absolute; left: 0; right: 0; top: 290px; text-align: center; font-family: "Prata", serif; font-size: 20px; color: var(--red); }

  .web-band { position: absolute; left: 0; right: 0; top: 336px; height: 22px; display: flex; align-items: center; }
  .web-band__bar { height: 12px; background: linear-gradient(90deg, var(--green), var(--orange) 55%, var(--red)); }
  .web-band__bar--left { width: 182px; }
  .web-band__bar--right { width: 180px; margin-left: auto; }
  .web-band__url { flex: 1; text-align: center; font-weight: 800; font-size: 19px; letter-spacing: 7px; color: var(--white); }
  .web-band__url .accent { color: var(--green); }

  .back__panel { position: absolute; left: 0; top: 0; width: 340px; height: 401px; background: var(--card-dark); }
  .card--back .brand-mark { left: 0; width: 340px; top: 118px; }
  .card--back .brand-mark__name { font-size: 27px; }
  .back__rule { position: absolute; left: 340px; top: 53px; width: 6px; height: 295px; background: linear-gradient(180deg, var(--red), var(--orange) 55%, #9bd417); }

  .owner { position: absolute; left: 366px; top: 84px; width: 282px; }
  .owner__name {
    font-family: "Cinzel", serif; font-weight: 700; font-size: 35px; line-height: 1;
    background: var(--brand-grad); -webkit-background-clip: text; background-clip: text; color: transparent;
  }
  .owner__title { font-size: 17px; font-weight: 500; letter-spacing: 6px; color: var(--ink); margin-top: 2px; padding-bottom: 1px; border-bottom: 1.5px solid var(--ink); }

  .contact-list { position: absolute; left: 365px; top: 180px; list-style: none; }
  .contact-list li { display: flex; align-items: center; height: 33px; font-size: 17px; color: var(--ink); }
  .contact-list svg { width: 16px; height: 16px; margin-right: 12px; flex: none; }

  .back__url { position: absolute; left: 366px; top: 322px; font-size: 17px; letter-spacing: 3.5px; color: var(--ink); }
  .back__url b { font-weight: 700; }
</style>
</head>
<body>

<section class="card card--front">
  <div class="brand-mark">
    <span class="brand-mark__dot"></span>
    <span class="brand-mark__name">Fontenot Bayou<br>Grillhouse</span>
  </div>
  <span class="verse__quote verse__quote--open">“</span>
  <p class="verse__lead">The LORD is my light and my salvation - whom shall I fear?</p>
  <p class="verse__follow">The LORD is the stronghold of my life - of whom shall I be afraid?</p>
  <p class="verse__ref">Psalms 27:1</p>
  <span class="verse__quote verse__quote--close">”</span>
  <div class="web-band">
    <span class="web-band__bar web-band__bar--left"></span>
    <span class="web-band__url">www.<span class="accent">fonbayou</span>.com</span>
    <span class="web-band__bar web-band__bar--right"></span>
  </div>
</section>

<section class="card card--back">
  <div class="back__panel">
    <div class="brand-mark">
      <span class="brand-mark__dot"></span>
      <span class="brand-mark__name">Fontenot Bayou<br>Grillhouse</span>
    </div>
  </div>
  <span class="back__rule"></span>

  <div class="owner">
    <h1 class="owner__name">Darvel Pruitt</h1>
    <p class="owner__title">OWNER</p>
  </div>

  <ul class="contact-list">
    <li>
      <svg viewBox="0 0 16 16"><rect width="16" height="16" rx="3" fill="#f20d0d"/><path d="M5 4.2c.5-.4 1-.3 1.3.2l.7 1.3c.2.4 0 .8-.3 1l-.5.4c.4.9 1.1 1.7 2 2.1l.4-.5c.3-.3.7-.4 1-.2l1.3.7c.5.3.5.8.2 1.3l-.6.7c-.5.5-1.3.5-2 .2C6.6 10.6 5.3 9.3 4.5 7.4c-.3-.7-.2-1.5.3-2z" fill="#fff"/></svg>
      (510) 493-2615
    </li>
    <li>
      <svg viewBox="0 0 16 16"><rect width="16" height="16" rx="3" fill="#f20d0d"/><rect x="3.5" y="5" width="9" height="6.5" fill="none" stroke="#fff" stroke-width="1.1"/><path d="M3.7 5.3 8 8.8l4.3-3.5" fill="none" stroke="#fff" stroke-width="1.1"/></svg>
      Dpruittkr4@mailvane.example
    </li>
    <li>
      <svg viewBox="0 0 16 16"><rect width="16" height="16" rx="3" fill="#f20d0d"/><path d="M8 3a3.2 3.2 0 0 0-3.2 3.2C4.8 8.6 8 12.5 8 12.5s3.2-3.9 3.2-6.3A3.2 3.2 0 0 0 8 3z" fill="#fff"/><circle cx="8" cy="6.2" r="1.2" fill="#f20d0d"/></svg>
      327 Oakmere Street
    </li>
  </ul>

  <p class="back__url">www.<b>fonbayou</b>.com</p>
</section>

</body>
</html>
```